Brightacre - online store for farm produce

Online store selling fresh produce (vegetables, fruits, dairy products, meat, ...) from various farmers. Every farm has its own shopping window - order page - just like a really simple web store.

Please check the attached design brief and mock-ups for further details.

Target Market(s)

People looking for fresh vegetables, fruit, meat, ... delivered from farms

Industry/Entity Type

Farming

Coding

Coded - Design and coding required

Number of Pages Required

5+ page

Font styles to use
Sans Serif

Requirements
Must have
• Custom design. Good UX/UI design, very functional.
Responsive using bootstrap 12 point grid system

```html
<!DOCTYPE html>
<html lang="en">
<head>
<meta charset="utf-8">
<title>Brightacre – Online Farm Produce Store</title>
<link href="https://fonts.googleapis.com/css2?family=Poppins:wght@400;500;600;700&display=swap" rel="stylesheet">
<style>
:root{
  --navy:#1c2a3a;
  --navy-soft:#223243;
  --frame:#3a4856;
  --label:#8794a3;
  --green:#7cb518;
  --mint:#abe6a6;
  --orange:#f0852b;
  --gold:#f6b81c;
  --ink:#1e2a36;
  --muted:#7c8691;
  --line:#e9edf1;
  --paper:#ffffff;
  --foot:#eef2f6;
}
*{box-sizing:border-box;margin:0;padding:0}
html,body{width:1200px;height:2749px;overflow:hidden}
body{background:var(--navy);font-family:'Poppins',sans-serif;color:var(--ink);position:relative}
.abs{position:absolute}
.top-rule{position:absolute;left:0;top:0;width:1200px;height:4px;background:var(--green)}
.backdrop-arc{position:absolute;left:-500px;top:1800px;width:2200px;height:2200px;border-radius:50%;background:var(--navy-soft)}
.produce-deco{position:absolute;border-radius:50%;filter:blur(2px)}
.brand-title{position:absolute;left:0;width:1200px;top:92px;text-align:center;font-size:86px;font-weight:700;color:#fff;letter-spacing:2px;line-height:1}
.board-label{position:absolute;font-size:28px;font-weight:600;color:var(--label);letter-spacing:1px}

.screen{position:absolute;background:var(--frame);padding:5px;box-shadow:0 20px 40px rgba(0,0,0,.35)}
.page{position:relative;background:var(--paper);width:100%;height:100%;overflow:hidden}

.nav{position:absolute;left:0;top:0;width:100%;height:34px;background:#fff;font-size:5.5px;font-weight:500}
.nav .logo{position:absolute;left:32px;top:11px;font-size:10px;font-weight:700;color:var(--ink);letter-spacing:.3px}
.nav .link{position:absolute;top:14px}
.nav .login{position:absolute;top:10px;width:36px;height:14px;border-radius:8px;background:var(--green);color:#fff;text-align:center;line-height:14px}
.hero{position:absolute;left:0;top:34px;width:100%;height:125px;background:var(--mint)}
.hero h1{position:absolute;left:33px;top:44px;font-size:21px;font-weight:600;color:#fff}
.hero .crumbs{position:absolute;left:34px;top:72px;font-size:6px;color:#fff;font-weight:500}
.hero .basket{position:absolute;right:0;top:10px;width:230px;height:115px;border-radius:110px 0 0 0;background:radial-gradient(circle at 55% 60%,#b3532c 0 22%,#d23b2f 23% 34%,#4f9a2a 35% 60%,rgba(171,230,166,0) 72%)}
.searchbar{position:absolute;left:77px;width:304px;height:24px;border-radius:12px;background:#fff;box-shadow:0 2px 8px rgba(0,0,0,.1);font-size:5.5px;color:#a1a8b0}
.searchbar .ph{position:absolute;left:12px;top:8px}
.searchbar .btn{position:absolute;right:2px;top:2px;width:54px;height:20px;border-radius:10px;background:var(--green);color:#fff;font-weight:600;text-align:center;line-height:20px}
.filters{position:absolute;left:115px;font-size:5px;font-weight:600}
.filters .lbl{position:absolute;left:0;top:4px}
.filters .pill{position:absolute;top:0;width:66px;height:14px;border-radius:7px;background:#eef1f4;text-align:center;line-height:14px;font-weight:500}
.result-label{position:absolute;left:33px;font-size:5px;font-weight:600}
.farm-card{position:absolute;width:128px;height:219px;background:#fff;box-shadow:0 2px 10px rgba(0,0,0,.09);border-radius:3px;padding:10px 9px;font-size:4.8px;color:var(--muted)}
.farm-card h3{font-size:9px;font-weight:600;color:var(--ink);line-height:1.1}
.farm-card .price{font-size:8px;font-weight:600;color:var(--orange)}
.farm-card .rating{position:absolute;right:9px;top:8px;font-size:4px;font-weight:600;color:var(--ink)}
.stars{color:var(--gold);font-size:6px;letter-spacing:-.5px}
.badges{display:flex;gap:2px;margin-top:2px}
.badges i{display:block;width:11px;height:11px;border-radius:50%;border:1.5px solid #2d6b3a;background:#e8f3e6}
.info{list-style:none;margin-top:12px}
.info li{display:flex;justify-content:space-between;height:10.5px}
.groups{margin-top:6px;background:#f7f9fb;padding:3px}
.groups div{display:flex;justify-content:space-between;height:18px;font-size:4.2px}
.groups b{display:block;color:var(--ink);font-size:4.5px}
.groups em{font-style:normal;color:var(--orange);font-weight:600;font-size:5px;align-self:center}
.order-btn{position:absolute;left:22px;bottom:9px;width:84px;height:14px;border-radius:8px;background:var(--green);color:#fff;font-size:4.5px;font-weight:600;text-align:center;line-height:14px}
.tile{position:absolute;width:76px;height:59px;background:#fff;box-shadow:0 2px 8px rgba(0,0,0,.08);text-align:center;padding-top:5px;font-size:4.2px;color:var(--muted)}
.tile b{display:block;font-size:6px;color:var(--ink);font-weight:600}
.tile .stars{display:block;margin-top:2px}
.tile .price{position:absolute;left:7px;bottom:6px;font-size:8px;font-weight:600;color:var(--orange)}
.tile svg{position:absolute;right:7px;bottom:8px}
.pager{position:absolute;left:0;width:100%;display:flex;justify-content:center;align-items:center;gap:6px;font-size:5px}
.pager .pp{padding:3px 7px;border-radius:7px;background:#eef1f4}
.pager .on{width:11px;height:11px;border-radius:50%;background:var(--orange);color:#fff;text-align:center;line-height:11px}
.pager .next{padding:3px 8px;border-radius:7px;background:var(--ink);color:#fff}
.produce-band{position:absolute;left:0;width:100%;height:62px;background:linear-gradient(90deg,#6aa83a,#c98a2a 35%,#b4473a 60%,#6aa83a)}
.footer{position:absolute;left:0;width:100%;height:210px;background:var(--foot)}
.footer h2{position:absolute;left:0;width:100%;top:18px;text-align:center;font-size:15px;font-weight:600}
.footer .nl{position:absolute;left:106px;top:44px;width:254px;height:18px;border-radius:9px;background:#fff;font-size:5.5px;color:#8a929b}
.footer .nl .ph{position:absolute;left:20px;top:5px}
.footer .nl svg{position:absolute;left:9px;top:6px}
.footer .nl .sub{position:absolute;right:0;top:0;width:64px;height:18px;border-radius:9px;background:var(--green);color:#fff;font-weight:600;text-align:center;line-height:18px;font-size:5px}
.footer .flogo{position:absolute;left:33px;top:102px;font-size:14px;font-weight:700;color:var(--ink)}
.footer .social{position:absolute;left:46px;top:122px;display:flex;gap:3px}
.footer .social i{display:block;width:12px;height:12px;border-radius:50%}
.footer .col{position:absolute;top:80px;font-size:5px;color:var(--muted);line-height:10.5px}
.footer .col h4{font-size:7px;color:var(--ink);font-weight:600;margin-bottom:5px}
.footer .col .ci{position:relative;padding-left:9px;margin-bottom:3px;line-height:7px}
.footer .col .ci b{color:var(--ink);font-weight:600;display:block}
.footer .col .ci svg{position:absolute;left:0;top:1px}
.footer .copy{position:absolute;left:0;width:100%;top:192px;text-align:center;font-size:5px;color:var(--ink)}
.footer .up{position:absolute;left:440px;top:168px;width:14px;height:14px;border-radius:50%;background:var(--orange)}
.footer .up svg{position:absolute;left:4px;top:4px}
.photo{position:absolute}
.sec-title{position:absolute;font-size:15px;font-weight:600;color:var(--ink);line-height:1.15}
.copy-text{position:absolute;font-size:5.5px;line-height:9px;color:var(--muted)}
.green-btn{position:absolute;height:16px;border-radius:8px;background:var(--green);color:#fff;font-size:4.8px;font-weight:600;text-align:center;line-height:16px}
.ticks{position:absolute;list-style:none;font-size:5.5px;color:var(--muted);line-height:12px}
.ticks li{padding-left:8px;position:relative}
.ticks li::before{content:"";position:absolute;left:0;top:4px;width:4px;height:4px;border-radius:50%;background:var(--mint)}
.form-card{position:absolute;background:linear-gradient(135deg,var(--green),#8fc62a);padding:10px 18px}
.form-card .field{height:16px;border-radius:8px;background:#fff;margin-bottom:7px;font-size:4.8px;color:#6e767e;padding:5px 10px;line-height:6px}
.form-card .tell{margin:10px auto 0;width:62px;height:16px;border-radius:8px;background:var(--orange);color:#fff;font-size:4.5px;font-weight:600;text-align:center;line-height:16px}
.ghost-word{position:absolute;font-size:72px;font-weight:700;color:#f1f3f5;letter-spacing:2px}
</style>
</head>
<body>

<div class="top-rule"></div>
<div class="backdrop-arc"></div>

<div class="produce-deco" role="img" aria-label="Fresh vegetables arranged in the corner" style="left:-30px;top:-20px;width:180px;height:140px;background:radial-gradient(circle at 40% 40%,#5aa532,#c7332b 45%,rgba(28,42,58,0) 70%)"></div>
<div class="produce-deco" role="img" aria-label="Pineapple, bananas and tropical fruit" style="left:-20px;top:1170px;width:135px;height:225px;background:radial-gradient(circle at 45% 50%,#e7b92c,#c2532b 40%,#5a8f2c 58%,rgba(28,42,58,0) 72%)"></div>
<div class="produce-deco" role="img" aria-label="Pile of fresh vegetables and fruit" style="left:-60px;top:2480px;width:520px;height:320px;background:radial-gradient(ellipse at 40% 60%,#d23b2f,#e2932a 30%,#4f9a2a 52%,rgba(34,50,67,0) 72%)"></div>

<div class="brand-title">BRIGHTACRE</div>

<div class="board-label" style="left:619px;top:255px">PRODUCT SEARCH</div>
<div class="board-label" style="left:114px;top:545px">DESKTOP</div>
<div class="board-label" style="left:619px;top:1670px">PRODUCT SEARCH</div>

<!-- ===== Product search: farm results ===== -->
<div class="screen" style="left:611px;top:306px;width:487px;height:1302px">
 <div class="page">
  <nav class="nav">
   <span class="logo">BRIGHTACRE</span>
   <span class="link" style="left:163px">HOME</span>
   <span class="link" style="left:200px">CURRENT OFFER</span>
   <span class="link" style="left:267px">SETTINGS</span>
   <span class="login" style="left:365px">LOGIN</span>
   <span class="link" style="left:408px">LOGOUT</span>
  </nav>
  <header class="hero">
   <div class="basket" role="img" aria-label="Wicker basket full of fresh vegetables"></div>
   <h1>Product Search</h1>
   <div class="crumbs">HOME | PRODUCT</div>
  </header>
  <div class="searchbar" style="top:188px"><span class="ph">Search product here...</span><span class="btn">SEARCH</span></div>
  <div class="filters" style="top:236px">
   <span class="lbl">FILTERS:</span>
   <span class="pill" style="left:28px">PRODUCT GROUP</span>
   <span class="pill" style="left:98px">REGION</span>
   <span class="pill" style="left:168px">DELIVERY METHOD</span>
  </div>
  <div class="result-label" style="top:266px">SEARCH RESULT FARM:</div>

  <article class="farm-card" style="left:32px;top:280px">
   <h3>Farm Name</h3><div class="price">$12.00</div>
   <div class="rating">RATING:<div class="stars">★★★★★</div>BADGES<div class="badges"><i></i><i></i></div></div>
   <ul class="info"><li>Farm Name<span>›</span></li><li>Address<span>›</span></li><li>Contact<span>›</span></li><li>Phone<span>›</span></li><li>Date of next delivery<span>›</span></li><li>Delivery methods<span>›</span></li><li>Minimal order Value<span>›</span></li></ul>
   <div class="groups"><div><span><b>PRODUCT GROUP 1</b>Onions, 3e/kg Tomatoe, e/kg</span><em>$12.00</em></div><div><span><b>PRODUCT GROUP 2</b>Onions, 3e/kg Tomatoe, e/kg</span><em>$12.00</em></div><div><span><b>PRODUCT GROUP 3</b>Onions, 3e/kg Tomatoe, e/kg</span><em>$12.00</em></div></div>
   <span class="order-btn">ORDER FROM THIS FARM</span>
  </article>
  <article class="farm-card" style="left:168px;top:280px">
   <h3>Farm Name</h3><div class="price">$12.00</div>
   <div class="rating">RATING:<div class="stars">★★★★★</div>BADGES<div class="badges"><i></i><i></i></div></div>
   <ul class="info"><li>Farm Name<span>›</span></li><li>Address<span>›</span></li><li>Contact<span>›</span></li><li>Phone<span>›</span></li><li>Date of next delivery<span>›</span></li><li>Delivery methods<span>›</span></li><li>Minimal order Value<span>›</span></li></ul>
   <div class="groups"><div><span><b>PRODUCT GROUP 1</b>Onions, 3e/kg Tomatoe, e/kg</span><em>$12.00</em></div><div><span><b>PRODUCT GROUP 2</b>Onions, 3e/kg Tomatoe, e/kg</span><em>$12.00</em></div><div><span><b>PRODUCT GROUP 3</b>Onions, 3e/kg Tomatoe, e/kg</span><em>$12.00</em></div></div>
   <span class="order-btn">ORDER FROM THIS FARM</span>
  </article>
  <article class="farm-card" style="left:303px;top:280px">
   <h3>Farm Name</h3><div class="price">$12.00</div>
   <div class="rating">RATING:<div class="stars">★★★★★</div>BADGES<div class="badges"><i></i><i></i></div></div>
   <ul class="info"><li>Farm Name<span>›</span></li><li>Address<span>›</span></li><li>Contact<span>›</span></li><li>Phone<span>›</span></li><li>Date of next delivery<span>›</span></li><li>Delivery methods<span>›</span></li><li>Minimal order Value<span>›</span></li></ul>
   <div class="groups"><div><span><b>PRODUCT GROUP 1</b>Onions, 3e/kg Tomatoe, e/kg</span><em>$12.00</em></div><div><span><b>PRODUCT GROUP 2</b>Onions, 3e/kg Tomatoe, e/kg</span><em>$12.00</em></div><div><span><b>PRODUCT GROUP 3</b>Onions, 3e/kg Tomatoe, e/kg</span><em>$12.00</em></div></div>
   <span class="order-btn">ORDER FROM THIS FARM</span>
  </article>

  <article class="farm-card" style="left:32px;top:508px">
   <h3>Farm Name</h3><div class="price">$12.00</div>
   <div class="rating">RATING:<div class="stars">★★★★★</div>BADGES<div class="badges"><i></i><i></i></div></div>
   <ul class="info"><li>Farm Name<span>›</span></li><li>Address<span>›</span></li><li>Contact<span>›</span></li><li>Phone<span>›</span></li><li>Date of next delivery<span>›</span></li><li>Delivery methods<span>›</span></li><li>Minimal order Value<span>›</span></li></ul>
   <div class="groups"><div><span><b>PRODUCT GROUP 1</b>Onions, 3e/kg Tomatoe, e/kg</span><em>$12.00</em></div><div><span><b>PRODUCT GROUP 2</b>Onions, 3e/kg Tomatoe, e/kg</span><em>$12.00</em></div><div><span><b>PRODUCT GROUP 3</b>Onions, 3e/kg Tomatoe, e/kg</span><em>$12.00</em></div></div>
   <span class="order-btn">ORDER FROM THIS FARM</span>
  </article>
  <article class="farm-card" style="left:168px;top:508px">
   <h3>Farm Name</h3><div class="price">$12.00</div>
   <div class="rating">RATING:<div class="stars">★★★★★</div>BADGES<div class="badges"><i></i><i></i></div></div>
   <ul class="info"><li>Farm Name<span>›</span></li><li>Address<span>›</span></li><li>Contact<span>›</span></li><li>Phone<span>›</span></li><li>Date of next delivery<span>›</span></li><li>Delivery methods<span>›</span></li><li>Minimal order Value<span>›</span></li></ul>
   <div class="groups"><div><span><b>PRODUCT GROUP 1</b>Onions, 3e/kg Tomatoe, e/kg</span><em>$12.00</em></div><div><span><b>PRODUCT GROUP 2</b>Onions, 3e/kg Tomatoe, e/kg</span><em>$12.00</em></div><div><span><b>PRODUCT GROUP 3</b>Onions, 3e/kg Tomatoe, e/kg</span><em>$12.00</em></div></div>
   <span class="order-btn">ORDER FROM THIS FARM</span>
  </article>
  <article class="farm-card" style="left:303px;top:508px">
   <h3>Farm Name</h3><div class="price">$12.00</div>
   <div class="rating">RATING:<div class="stars">★★★★★</div>BADGES<div class="badges"><i></i><i></i></div></div>
   <ul class="info"><li>Farm Name<span>›</span></li><li>Address<span>›</span></li><li>Contact<span>›</span></li><li>Phone<span>›</span></li><li>Date of next delivery<span>›</span></li><li>Delivery methods<span>›</span></li><li>Minimal order Value<span>›</span></li></ul>
   <div class="groups"><div><span><b>PRODUCT GROUP 1</b>Onions, 3e/kg Tomatoe, e/kg</span><em>$12.00</em></div><div><span><b>PRODUCT GROUP 2</b>Onions, 3e/kg Tomatoe, e/kg</span><em>$12.00</em></div><div><span><b>PRODUCT GROUP 3</b>Onions, 3e/kg Tomatoe, e/kg</span><em>$12.00</em></div></div>
   <span class="order-btn">ORDER FROM THIS FARM</span>
  </article>

  <article class="farm-card" style="left:32px;top:736px">
   <h3>Farm Name</h3><div class="price">$12.00</div>
   <div class="rating">RATING:<div class="stars">★★★★★</div>BADGES<div class="badges"><i></i><i></i></div></div>
   <ul class="info"><li>Farm Name<span>›</span></li><li>Address<span>›</span></li><li>Contact<span>›</span></li><li>Phone<span>›</span></li><li>Date of next delivery<span>›</span></li><li>Delivery methods<span>›</span></li><li>Minimal order Value<span>›</span></li></ul>
   <div class="groups"><div><span><b>PRODUCT GROUP 1</b>Onions, 3e/kg Tomatoe, e/kg</span><em>$12.00</em></div><div><span><b>PRODUCT GROUP 2</b>Onions, 3e/kg Tomatoe, e/kg</span><em>$12.00</em></div><div><span><b>PRODUCT GROUP 3</b>Onions, 3e/kg Tomatoe, e/kg</span><em>$12.00</em></div></div>
   <span class="order-btn">ORDER FROM THIS FARM</span>
  </article>
  <article class="farm-card" style="left:168px;top:736px">
   <h3>Farm Name</h3><div class="price">$12.00</div>
   <div class="rating">RATING:<div class="stars">★★★★★</div>BADGES<div class="badges"><i></i><i></i></div></div>
   <ul class="info"><li>Farm Name<span>›</span></li><li>Address<span>›</span></li><li>Contact<span>›</span></li><li>Phone<span>›</span></li><li>Date of next delivery<span>›</span></li><li>Delivery methods<span>›</span></li><li>Minimal order Value<span>›</span></li></ul>
   <div class="groups"><div><span><b>PRODUCT GROUP 1</b>Onions, 3e/kg Tomatoe, e/kg</span><em>$12.00</em></div><div><span><b>PRODUCT GROUP 2</b>Onions, 3e/kg Tomatoe, e/kg</span><em>$12.00</em></div><div><span><b>PRODUCT GROUP 3</b>Onions, 3e/kg Tomatoe, e/kg</span><em>$12.00</em></div></div>
   <span class="order-btn">ORDER FROM THIS FARM</span>
  </article>
  <article class="farm-card" style="left:303px;top:736px">
   <h3>Farm Name</h3><div class="price">$12.00</div>
   <div class="rating">RATING:<div class="stars">★★★★★</div>BADGES<div class="badges"><i></i><i></i></div></div>
   <ul class="info"><li>Farm Name<span>›</span></li><li>Address<span>›</span></li><li>Contact<span>›</span></li><li>Phone<span>›</span></li><li>Date of next delivery<span>›</span></li><li>Delivery methods<span>›</span></li><li>Minimal order Value<span>›</span></li></ul>
   <div class="groups"><div><span><b>PRODUCT GROUP 1</b>Onions, 3e/kg Tomatoe, e/kg</span><em>$12.00</em></div><div><span><b>PRODUCT GROUP 2</b>Onions, 3e/kg Tomatoe, e/kg</span><em>$12.00</em></div><div><span><b>PRODUCT GROUP 3</b>Onions, 3e/kg Tomatoe, e/kg</span><em>$12.00</em></div></div>
   <span class="order-btn">ORDER FROM THIS FARM</span>
  </article>

  <div class="pager" style="top:984px"><span class="pp">‹ Prev</span><span>1</span><span class="on">2</span><span>3</span><span>...</span><span>82</span><span class="next">Next ›</span></div>
  <div class="produce-band" style="top:1024px" role="img" aria-label="Row of fresh vegetables"></div>
  <footer class="footer" style="top:1086px">
   <h2>Newsletter</h2>
   <div class="nl"><svg width="7" height="5" viewBox="0 0 7 5"><rect x=".3" y=".3" width="6.4" height="4.4" fill="none" stroke="#9aa1a8" stroke-width=".6"/><path d="M.3.3 3.5 3 6.7.3" fill="none" stroke="#9aa1a8" stroke-width=".6"/></svg><span class="ph">Enter your email address</span><span class="sub">SUBSCRIBE</span></div>
   <div class="flogo">BRIGHTACRE</div>
   <div class="social"><i style="background:#3b5998"></i><i style="background:#1da1f2"></i><i style="background:#dd4b39"></i><i style="background:#c13584"></i></div>
   <div class="col" style="left:154px"><h4>Quick Links</h4>Home<br>Current Offer<br>Settings<br>Login/Logout</div>
   <div class="col" style="left:243px"><h4>Information</h4>Terms of use<br>Terms and Conditions<br>Privacy Policy<br>About Us<br>FAQ</div>
   <div class="col" style="left:343px"><h4>Contact Info</h4>
    <div class="ci"><svg width="5" height="5" viewBox="0 0 5 5"><path d="M1 0 2 1.5 1.4 2.2Q2 3.3 2.8 3.6L3.5 3 5 4 4.3 5Q1 4.5 0 .8Z" fill="var(--orange)"/></svg><b>Phone</b>+08 123 456 7890</div>
    <div class="ci"><svg width="5" height="4" viewBox="0 0 5 4"><rect width="5" height="4" fill="var(--orange)"/></svg><b>Email</b>info@example.com</div>
    <div class="ci"><svg width="4" height="6" viewBox="0 0 4 6"><path d="M2 6 0 2.5A2 2 0 1 1 4 2.5Z" fill="var(--orange)"/></svg><b>Location</b>Some address line goes here<br>city name country</div>
   </div>
   <div class="copy">© 2020 Copyright - Harvestline All Rights Reserved</div>
   <div class="up"><svg width="6" height="5" viewBox="0 0 6 5"><path d="M.5 4 3 1.2 5.5 4" fill="none" stroke="#fff" stroke-width="1"/></svg></div>
  </footer>
 </div>
</div>

<!-- ===== Desktop landing ===== -->
<div class="screen" style="left:107px;top:597px;width:478px;height:1619px">
 <div class="page">
  <nav class="nav">
   <span class="logo">BRIGHTACRE</span>
   <span class="link" style="left:167px">HOME</span>
   <span class="link" style="left:204px">CURRENT OFFER</span>
   <span class="link" style="left:271px">SETTINGS</span>
   <span class="login" style="left:370px">LOGIN</span>
   <span class="link" style="left:410px">LOGOUT</span>
  </nav>
  <div class="photo" role="img" aria-label="Market stall crates filled with colourful vegetables" style="left:0;top:35px;width:100%;height:230px;background:linear-gradient(120deg,#6f4a2a,#3f6f2a 30%,#b2432b 55%,#5d8f2c 75%,#d1a23a)"></div>
  <svg class="abs" style="left:0;top:180px" width="467" height="230" viewBox="0 0 467 230"><path d="M0 62Q25 30 70 60Q95 80 110 85L100 86Q60 95 45 120Q30 150 0 190Z" fill="var(--orange)"/><path d="M70 84Q200 84 467 84L467 230L0 230L0 190Q30 150 45 120Q60 95 100 86Z" fill="#fff"/></svg>
  <div class="abs" style="left:34px;top:108px;font-size:6px;font-weight:600;color:#fff">EXTRA 50% OFF FOR ALL PRODUCT</div>
  <div class="abs" style="left:33px;top:118px;font-size:21px;font-weight:600;color:#fff;line-height:24px">Build Your Health<br>Eating Brightacre</div>
  <div class="green-btn" style="left:34px;top:174px;width:74px;background:var(--orange)">▶ WATCH A VIDEO PLAY</div>
  <div class="abs" style="left:80px;top:248px;width:18px;height:18px;border-radius:50%;background:var(--mint)"></div>

  <div class="photo" role="img" aria-label="Raw meat with vegetables on a cutting board" style="left:53px;top:284px;width:174px;height:174px;background:linear-gradient(135deg,#7a2f26,#c86b5c 45%,#e8d2c0);box-shadow:0 8px 18px rgba(0,0,0,.18)"></div>
  <h2 class="sec-title" style="left:257px;top:308px">What is this about</h2>
  <div class="abs" style="left:257px;top:331px;width:24px;height:1px;background:var(--line)"></div>
  <p class="copy-text" style="left:257px;top:336px;width:180px">Lorem ipsum dolor sit amet, consectetur adipisicing elit, sed do eiusmod tempor incididunt ut labore et dolore magna aliqua. Ut enim ad minim veniam, quis nostrud exercitation ullamco laboris nisi ut aliquip ex ea commodo consequat. Duis aute irure dolor in reprehenderit in voluptate velit esse cillum dolore eu fugiat nulla pariatur.</p>
  <p class="copy-text" style="left:257px;top:399px;width:180px">Excepteur sint runt mollit anim id est laborum. Sed ut atis unde omnis iste natus error sit volu</p>
  <span class="green-btn" style="left:257px;top:432px;width:64px">PRODUCT SEARCH</span>

  <div class="abs" style="left:420px;top:502px;width:48px;height:58px;border-radius:50%;background:#e3f5e0"></div>
  <h2 class="sec-title" style="left:34px;top:535px">Customer benefits</h2>
  <ul class="ticks" style="left:34px;top:559px">
   <li>Lorem ipsum dolor sit amet consectetur adipisicing elit,</li><li>Sed do eiusmod tempor incididunt ut labore</li><li>Ut enim ad minim veniam nostrud exercitation ullamco</li><li>laboris nisi ut aliquip ex ea commodo consequat.</li><li>Duis aute irure dolor in reprehenderit</li><li>velit esse cillum dolore eu fugiat nulla pariatur. Excepteur</li><li>Sint occaecat cupidatat non proident,</li><li>Sunt in culpa qui deserunt mollit anim id est laborum</li>
  </ul>
  <span class="green-btn" style="left:34px;top:664px;width:64px">PRODUCT SEARCH</span>
  <div class="photo" role="img" aria-label="Shopper holding a paper bag of fresh greens" style="left:261px;top:522px;width:170px;height:204px;background:linear-gradient(160deg,#e8ece6,#6c9b4a 45%,#b98a5c 75%,#8a4b3a)"></div>

  <h2 class="sec-title" style="left:0;width:100%;text-align:center;top:742px">Farmer benefits</h2>
  <ul class="ticks" style="left:50px;top:772px"><li>Lorem ipsum dolor sit amet consectetur adipisicing elit,</li><li>Sed do eiusmod tempor incididunt ut labore</li><li>Ut enim ad minim veniam nostrud exercitation ullamco</li><li>laboris nisi ut aliquip ex ea commodo consequat.</li></ul>
  <ul class="ticks" style="left:241px;top:772px"><li>Duis aute irure dolor in reprehenderit</li><li>velit esse cillum dolore eu fugiat nulla pariatur. Excepteur</li><li>Sint occaecat cupidatat non proident,</li><li>Sunt in culpa qui deserunt mollit anim id est laborum</li></ul>

  <div class="ghost-word" style="left:100px;top:1005px">Farmers</div>
  <div class="photo" role="img" aria-label="Farmer in a straw hat carrying a crate of vegetables in a field" style="left:154px;top:830px;width:279px;height:186px;background:linear-gradient(120deg,#cfe3ea,#7fa84a 40%,#4f7d2c 70%,#d98a3a)"></div>
  <div class="abs" style="left:118px;top:843px;width:90px;height:125px;border:2px solid var(--green)"></div>
  <form class="form-card" style="left:35px;top:853px;width:176px;height:117px">
   <div class="field">Company Name*</div><div class="field">Full Name*</div><div class="field">E-mail*</div>
   <div class="tell">TELL ME MORE</div>
  </form>

  <div class="abs" style="left:0;top:1270px;width:50px;height:90px;border-radius:0 50px 50px 0;background:#e3f5e0"></div>
  <div class="photo" role="img" aria-label="Farmer with a tablet in a cattle barn" style="left:36px;top:1142px;width:189px;height:167px;background:linear-gradient(150deg,#cbb891,#6f8fae 45%,#2f3a3f 75%,#9a8a62)"></div>
  <h2 class="sec-title" style="left:257px;top:1146px">Featured farm or<br>product</h2>
  <div class="abs" style="left:257px;top:1184px;width:24px;height:1px;background:var(--line)"></div>
  <p class="copy-text" style="left:257px;top:1188px;width:180px">Lorem ipsum dolor sit amet, consectetur adipisicing elit, sed do eiusmod tempor incididunt ut labore et dolore magna aliqua. Ut enim ad minim veniam, quis nostrud exercitation ullamco laboris nisi ut aliquip ex ea commodo consequat. Duis aute irure dolor in reprehenderit in voluptate velit esse cillum dolore eu fugiat nulla pariatur.</p>
  <p class="copy-text" style="left:257px;top:1251px;width:180px">Excepteur sint runt mollit anim id est laborum. Sed ut atis unde omnis iste natus error sit volu</p>
  <span class="green-btn" style="left:257px;top:1286px;width:64px">OUR FARM</span>

  <div class="produce-band" style="top:1343px" role="img" aria-label="Row of fresh vegetables"></div>
  <footer class="footer" style="top:1404px">
   <h2>Newsletter</h2>
   <div class="nl"><svg width="7" height="5" viewBox="0 0 7 5"><rect x=".3" y=".3" width="6.4" height="4.4" fill="none" stroke="#9aa1a8" stroke-width=".6"/><path d="M.3.3 3.5 3 6.7.3" fill="none" stroke="#9aa1a8" stroke-width=".6"/></svg><span class="ph">Enter your email address</span><span class="sub">SUBSCRIBE</span></div>
   <div class="flogo">BRIGHTACRE</div>
   <div class="social"><i style="background:#3b5998"></i><i style="background:#1da1f2"></i><i style="background:#dd4b39"></i><i style="background:#c13584"></i></div>
   <div class="col" style="left:154px"><h4>Quick Links</h4>Home<br>Current Offer<br>Settings<br>Login/Logout</div>
   <div class="col" style="left:243px"><h4>Information</h4>Terms of use<br>Terms and Conditions<br>Privacy Policy<br>About Us<br>FAQ</div>
   <div class="col" style="left:343px"><h4>Contact Info</h4>
    <div class="ci"><svg width="5" height="5" viewBox="0 0 5 5"><path d="M1 0 2 1.5 1.4 2.2Q2 3.3 2.8 3.6L3.5 3 5 4 4.3 5Q1 4.5 0 .8Z" fill="var(--orange)"/></svg><b>Phone</b>+08 123 456 7890</div>
    <div class="ci"><svg width="5" height="4" viewBox="0 0 5 4"><rect width="5" height="4" fill="var(--orange)"/></svg><b>Email</b>info@example.com</div>
    <div class="ci"><svg width="4" height="6" viewBox="0 0 4 6"><path d="M2 6 0 2.5A2 2 0 1 1 4 2.5Z" fill="var(--orange)"/></svg><b>Location</b>Some address line goes here<br>city name country</div>
   </div>
   <div class="copy">© 2020 Copyright - Harvestline All Rights Reserved</div>
   <div class="up"><svg width="6" height="5" viewBox="0 0 6 5"><path d="M.5 4 3 1.2 5.5 4" fill="none" stroke="#fff" stroke-width="1"/></svg></div>
  </footer>
 </div>
</div>

<!-- ===== Product search: product results ===== -->
<div class="screen" style="left:611px;top:1722px;width:487px;height:894px">
 <div class="page">
  <nav class="nav">
   <span class="logo">BRIGHTACRE</span>
   <span class="link" style="left:163px">HOME</span>
   <span class="link" style="left:200px">CURRENT OFFER</span>
   <span class="link" style="left:267px">SETTINGS</span>
   <span class="login" style="left:365px">LOGIN</span>
   <span class="link" style="left:408px">LOGOUT</span>
  </nav>
  <header class="hero">
   <div class="basket" role="img" aria-label="Wicker basket full of fresh vegetables"></div>
   <h1>Product Search</h1>
   <div class="crumbs">HOME | PRODUCT</div>
  </header>
  <div class="searchbar" style="top:188px"><span class="ph">Search product here...</span><span class="btn">SEARCH</span></div>
  <div class="filters" style="top:236px">
   <span class="lbl">FILTERS:</span>
   <span class="pill" style="left:28px">PRODUCT GROUP</span>
   <span class="pill" style="left:98px">REGION</span>
   <span class="pill" style="left:168px">DELIVERY METHOD</span>
  </div>
  <div class="result-label" style="top:266px">SEARCH RESULT FARM:</div>

  <div class="tile" style="left:32px;top:281px"><b>Product name</b>Onions, 3e/kg Tomatoe, e/kg<span class="stars">★★★★★</span><span class="price">$12.00</span><svg width="7" height="6" viewBox="0 0 7 6"><path d="M0 .5H1.3L2.2 4.2H6L6.6 1.5H1.6" fill="none" stroke="#555" stroke-width=".6"/><circle cx="2.6" cy="5.4" r=".5" fill="#555"/><circle cx="5.5" cy="5.4" r=".5" fill="#555"/></svg></div>
  <div class="tile" style="left:112px;top:281px"><b>Product name</b>Onions, 3e/kg Tomatoe, e/kg<span class="stars">★★★★★</span><span class="price">$12.00</span><svg width="7" height="6" viewBox="0 0 7 6"><path d="M0 .5H1.3L2.2 4.2H6L6.6 1.5H1.6" fill="none" stroke="#555" stroke-width=".6"/><circle cx="2.6" cy="5.4" r=".5" fill="#555"/><circle cx="5.5" cy="5.4" r=".5" fill="#555"/></svg></div>
  <div class="tile" style="left:192px;top:281px"><b>Product name</b>Onions, 3e/kg Tomatoe, e/kg<span class="stars">★★★★★</span><span class="price">$12.00</span><svg width="7" height="6" viewBox="0 0 7 6"><path d="M0 .5H1.3L2.2 4.2H6L6.6 1.5H1.6" fill="none" stroke="#555" stroke-width=".6"/><circle cx="2.6" cy="5.4" r=".5" fill="#555"/><circle cx="5.5" cy="5.4" r=".5" fill="#555"/></svg></div>
  <div class="tile" style="left:272px;top:281px"><b>Product name</b>Onions, 3e/kg Tomatoe, e/kg<span class="stars">★★★★★</span><span class="price">$12.00</span><svg width="7" height="6" viewBox="0 0 7 6"><path d="M0 .5H1.3L2.2 4.2H6L6.6 1.5H1.6" fill="none" stroke="#555" stroke-width=".6"/><circle cx="2.6" cy="5.4" r=".5" fill="#555"/><circle cx="5.5" cy="5.4" r=".5" fill="#555"/></svg></div>
  <div class="tile" style="left:352px;top:281px"><b>Product name</b>Onions, 3e/kg Tomatoe, e/kg<span class="stars">★★★★★</span><span class="price">$12.00</span><svg width="7" height="6" viewBox="0 0 7 6"><path d="M0 .5H1.3L2.2 4.2H6L6.6 1.5H1.6" fill="none" stroke="#555" stroke-width=".6"/><circle cx="2.6" cy="5.4" r=".5" fill="#555"/><circle cx="5.5" cy="5.4" r=".5" fill="#555"/></svg></div>

  <div class="tile" style="left:32px;top:347px"><b>Product name</b>Onions, 3e/kg Tomatoe, e/kg<span class="stars">★★★★★</span><span class="price">$12.00</span><svg width="7" height="6" viewBox="0 0 7 6"><path d="M0 .5H1.3L2.2 4.2H6L6.6 1.5H1.6" fill="none" stroke="#555" stroke-width=".6"/><circle cx="2.6" cy="5.4" r=".5" fill="#555"/><circle cx="5.5" cy="5.4" r=".5" fill="#555"/></svg></div>
  <div class="tile" style="left:112px;top:347px"><b>Product name</b>Onions, 3e/kg Tomatoe, e/kg<span class="stars">★★★★★</span><span class="price">$12.00</span><svg width="7" height="6" viewBox="0 0 7 6"><path d="M0 .5H1.3L2.2 4.2H6L6.6 1.5H1.6" fill="none" stroke="#555" stroke-width=".6"/><circle cx="2.6" cy="5.4" r=".5" fill="#555"/><circle cx="5.5" cy="5.4" r=".5" fill="#555"/></svg></div>
  <div class="tile" style="left:192px;top:347px"><b>Product name</b>Onions, 3e/kg Tomatoe, e/kg<span class="stars">★★★★★</span><span class="price">$12.00</span><svg width="7" height="6" viewBox="0 0 7 6"><path d="M0 .5H1.3L2.2 4.2H6L6.6 1.5H1.6" fill="none" stroke="#555" stroke-width=".6"/><circle cx="2.6" cy="5.4" r=".5" fill="#555"/><circle cx="5.5" cy="5.4" r=".5" fill="#555"/></svg></div>
  <div class="tile" style="left:272px;top:347px"><b>Product name</b>Onions, 3e/kg Tomatoe, e/kg<span class="stars">★★★★★</span><span class="price">$12.00</span><svg width="7" height="6" viewBox="0 0 7 6"><path d="M0 .5H1.3L2.2 4.2H6L6.6 1.5H1.6" fill="none" stroke="#555" stroke-width=".6"/><circle cx="2.6" cy="5.4" r=".5" fill="#555"/><circle cx="5.5" cy="5.4" r=".5" fill="#555"/></svg></div>
  <div class="tile" style="left:352px;top:347px"><b>Product name</b>Onions, 3e/kg Tomatoe, e/kg<span class="stars">★★★★★</span><span class="price">$12.00</span><svg width="7" height="6" viewBox="0 0 7 6"><path d="M0 .5H1.3L2.2 4.2H6L6.6 1.5H1.6" fill="none" stroke="#555" stroke-width=".6"/><circle cx="2.6" cy="5.4" r=".5" fill="#555"/><circle cx="5.5" cy="5.4" r=".5" fill="#555"/></svg></div>

  <div class="tile" style="left:32px;top:414px"><b>Product name</b>Onions, 3e/kg Tomatoe, e/kg<span class="stars">★★★★★</span><span class="price">$12.00</span><svg width="7" height="6" viewBox="0 0 7 6"><path d="M0 .5H1.3L2.2 4.2H6L6.6 1.5H1.6" fill="none" stroke="#555" stroke-width=".6"/><circle cx="2.6" cy="5.4" r=".5" fill="#555"/><circle cx="5.5" cy="5.4" r=".5" fill="#555"/></svg></div>
  <div class="tile" style="left:112px;top:414px"><b>Product name</b>Onions, 3e/kg Tomatoe, e/kg<span class="stars">★★★★★</span><span class="price">$12.00</span><svg width="7" height="6" viewBox="0 0 7 6"><path d="M0 .5H1.3L2.2 4.2H6L6.6 1.5H1.6" fill="none" stroke="#555" stroke-width=".6"/><circle cx="2.6" cy="5.4" r=".5" fill="#555"/><circle cx="5.5" cy="5.4" r=".5" fill="#555"/></svg></div>
  <div class="tile" style="left:192px;top:414px"><b>Product name</b>Onions, 3e/kg Tomatoe, e/kg<span class="stars">★★★★★</span><span class="price">$12.00</span><svg width="7" height="6" viewBox="0 0 7 6"><path d="M0 .5H1.3L2.2 4.2H6L6.6 1.5H1.6" fill="none" stroke="#555" stroke-width=".6"/><circle cx="2.6" cy="5.4" r=".5" fill="#555"/><circle cx="5.5" cy="5.4" r=".5" fill="#555"/></svg></div>
  <div class="tile" style="left:272px;top:414px"><b>Product name</b>Onions, 3e/kg Tomatoe, e/kg<span class="stars">★★★★★</span><span class="price">$12.00</span><svg width="7" height="6" viewBox="0 0 7 6"><path d="M0 .5H1.3L2.2 4.2H6L6.6 1.5H1.6" fill="none" stroke="#555" stroke-width=".6"/><circle cx="2.6" cy="5.4" r=".5" fill="#555"/><circle cx="5.5" cy="5.4" r=".5" fill="#555"/></svg></div>
  <div class="tile" style="left:352px;top:414px"><b>Product name</b>Onions, 3e/kg Tomatoe, e/kg<span class="stars">★★★★★</span><span class="price">$12.00</span><svg width="7" height="6" viewBox="0 0 7 6"><path d="M0 .5H1.3L2.2 4.2H6L6.6 1.5H1.6" fill="none" stroke="#555" stroke-width=".6"/><circle cx="2.6" cy="5.4" r=".5" fill="#555"/><circle cx="5.5" cy="5.4" r=".5" fill="#555"/></svg></div>

  <div class="tile" style="left:32px;top:480px"><b>Product name</b>Onions, 3e/kg Tomatoe, e/kg<span class="stars">★★★★★</span><span class="price">$12.00</span><svg width="7" height="6" viewBox="0 0 7 6"><path d="M0 .5H1.3L2.2 4.2H6L6.6 1.5H1.6" fill="none" stroke="#555" stroke-width=".6"/><circle cx="2.6" cy="5.4" r=".5" fill="#555"/><circle cx="5.5" cy="5.4" r=".5" fill="#555"/></svg></div>
  <div class="tile" style="left:112px;top:480px"><b>Product name</b>Onions, 3e/kg Tomatoe, e/kg<span class="stars">★★★★★</span><span class="price">$12.00</span><svg width="7" height="6" viewBox="0 0 7 6"><path d="M0 .5H1.3L2.2 4.2H6L6.6 1.5H1.6" fill="none" stroke="#555" stroke-width=".6"/><circle cx="2.6" cy="5.4" r=".5" fill="#555"/><circle cx="5.5" cy="5.4" r=".5" fill="#555"/></svg></div>
  <div class="tile" style="left:192px;top:480px"><b>Product name</b>Onions, 3e/kg Tomatoe, e/kg<span class="stars">★★★★★</span><span class="price">$12.00</span><svg width="7" height="6" viewBox="0 0 7 6"><path d="M0 .5H1.3L2.2 4.2H6L6.6 1.5H1.6" fill="none" stroke="#555" stroke-width=".6"/><circle cx="2.6" cy="5.4" r=".5" fill="#555"/><circle cx="5.5" cy="5.4" r=".5" fill="#555"/></svg></div>
  <div class="tile" style="left:272px;top:480px"><b>Product name</b>Onions, 3e/kg Tomatoe, e/kg<span class="stars">★★★★★</span><span class="price">$12.00</span><svg width="7" height="6" viewBox="0 0 7 6"><path d="M0 .5H1.3L2.2 4.2H6L6.6 1.5H1.6" fill="none" stroke="#555" stroke-width=".6"/><circle cx="2.6" cy="5.4" r=".5" fill="#555"/><circle cx="5.5" cy="5.4" r=".5" fill="#555"/></svg></div>
  <div class="tile" style="left:352px;top:480px"><b>Product name</b>Onions, 3e/kg Tomatoe, e/kg<span class="stars">★★★★★</span><span class="price">$12.00</span><svg width="7" height="6" viewBox="0 0 7 6"><path d="M0 .5H1.3L2.2 4.2H6L6.6 1.5H1.6" fill="none" stroke="#555" stroke-width=".6"/><circle cx="2.6" cy="5.4" r=".5" fill="#555"/><circle cx="5.5" cy="5.4" r=".5" fill="#555"/></svg></div>

  <div class="pager" style="top:570px"><span class="pp">‹ Prev</span><span>1</span><span class="on">2</span><span>3</span><span>...</span><span>82</span><span class="next">Next ›</span></div>
  <div class="produce-band" style="top:610px" role="img" aria-label="Row of fresh vegetables"></div>
  <footer class="footer" style="top:672px">
   <h2>Newsletter</h2>
   <div class="nl"><svg width="7" height="5" viewBox="0 0 7 5"><rect x=".3" y=".3" width="6.4" height="4.4" fill="none" stroke="#9aa1a8" stroke-width=".6"/><path d="M.3.3 3.5 3 6.7.3" fill="none" stroke="#9aa1a8" stroke-width=".6"/></svg><span class="ph">Enter your email address</span><span class="sub">SUBSCRIBE</span></div>
   <div class="flogo">BRIGHTACRE</div>
   <div class="social"><i style="background:#3b5998"></i><i style="background:#1da1f2"></i><i style="background:#dd4b39"></i><i style="background:#c13584"></i></div>
   <div class="col" style="left:154px"><h4>Quick Links</h4>Home<br>Current Offer<br>Settings<br>Login/Logout</div>
   <div class="col" style="left:243px"><h4>Information</h4>Terms of use<br>Terms and Conditions<br>Privacy Policy<br>About Us<br>FAQ</div>
   <div class="col" style="left:343px"><h4>Contact Info</h4>
    <div class="ci"><svg width="5" height="5" viewBox="0 0 5 5"><path d="M1 0 2 1.5 1.4 2.2Q2 3.3 2.8 3.6L3.5 3 5 4 4.3 5Q1 4.5 0 .8Z" fill="var(--orange)"/></svg><b>Phone</b>+08 123 456 7890</div>
    <div class="ci"><svg width="5" height="4" viewBox="0 0 5 4"><rect width="5" height="4" fill="var(--orange)"/></svg><b>Email</b>info@example.com</div>
    <div class="ci"><svg width="4" height="6" viewBox="0 0 4 6"><path d="M2 6 0 2.5A2 2 0 1 1 4 2.5Z" fill="var(--orange)"/></svg><b>Location</b>Some address line goes here<br>city name country</div>
   </div>
   <div class="copy">© 2020 Copyright - Harvestline All Rights Reserved</div>
   <div class="up"><svg width="6" height="5" viewBox="0 0 6 5"><path d="M.5 4 3 1.2 5.5 4" fill="none" stroke="#fff" stroke-width="1"/></svg></div>
  </footer>
 </div>
</div>

</body>
</html>
```